Commercial Insurance Agency needs a design for a trade show retractable display.

We need a design for a retractable banner or display for a trade show. We are a commercial insurance agency that specializes in placing and servicing workers comp insurance for large companies. We want to use our company colors which are orange, grey and charcoal.

Font styles to use
Sans Serif

Requirements
Must have
• Our orange color that is on the style sheet should be the secondary color...we don't want the whole thing to be orange

```html
<!DOCTYPE html>
<html lang="en">
<head>
<meta charset="utf-8">
<title>CIRCA – Trade Show Retractable Banner</title>
<link href="https://fonts.googleapis.com/css2?family=Poppins:ital,wght@0,600;1,800&family=Arimo:wght@400&display=swap" rel="stylesheet">
<style>
  :root {
    --bg: #eef1f5;
    --charcoal: #2c3649;
    --slate: #4a5262;
    --grey: #767a83;
    --orange: #f2642a;
    --orange-deep: #d9431c;
    --white: #ffffff;
  }
  html, body {
    margin: 0;
    padding: 0;
    width: 1200px;
    height: 1200px;
    overflow: hidden;
    background: var(--bg);
  }
  .banner {
    position: absolute;
    left: 330px;
    top: 45px;
    width: 540px;
    height: 1110px;
    overflow: hidden;
    font-family: "Arimo", Arial, sans-serif;
    color: var(--white);
  }
  .banner-art {
    position: absolute;
    inset: 0;
  }
  .brand-name {
    position: absolute;
    right: 48px;
    top: 78px;
    font-family: "Poppins", Arial, sans-serif;
    font-weight: 600;
    font-size: 50px;
    letter-spacing: 2px;
    color: var(--white);
    line-height: 1;
  }
  .service {
    position: absolute;
    left: 0;
    width: 100%;
  }
  .service-icon {
    position: absolute;
    left: 36px;
    top: 0;
    width: 50px;
    height: 50px;
  }
  .service-title {
    position: absolute;
    left: 108px;
    top: 0;
    margin: 0;
    font-family: "Poppins", Arial, sans-serif;
    font-style: italic;
    font-weight: 800;
    font-size: 31px;
    line-height: 40px;
    letter-spacing: 0.5px;
  }
  .service-text {
    position: absolute;
    left: 116px;
    top: 40px;
    margin: 0;
    font-size: 20px;
    line-height: 24px;
    white-space: nowrap;
  }
  .service--compliance { top: 438px; }
  .service--claims { top: 556px; }
  .service--profit { top: 672px; }
  .cta-pill {
    position: absolute;
    left: 118px;
    top: 831px;
    width: 304px;
    height: 31px;
    background: var(--orange);
    border-radius: 5px;
    font-size: 19px;
    line-height: 31px;
    text-align: center;
  }
  .cta-phone {
    position: absolute;
    left: 0;
    width: 100%;
    top: 870px;
    text-align: center;
    font-family: "Poppins", Arial, sans-serif;
    font-style: italic;
    font-weight: 800;
    font-size: 52px;
    line-height: 60px;
    letter-spacing: 1px;
  }
  .site-url {
    position: absolute;
    left: 0;
    width: 100%;
    top: 1020px;
    text-align: center;
    font-size: 22px;
  }
</style>
</head>
<body>
  <main class="banner">
    <svg class="banner-art" width="540" height="1110" viewBox="0 0 540 1110">
      <defs>
        <linearGradient id="photoTone" x1="0" y1="0" x2="1" y2="1">
          <stop offset="0" stop-color="#c9c3b2"/>
          <stop offset="0.45" stop-color="#8d8a7d"/>
          <stop offset="1" stop-color="#b59a4a"/>
        </linearGradient>
        <linearGradient id="panelTone" x1="0" y1="0" x2="0" y2="1">
          <stop offset="0" stop-color="#253146"/>
          <stop offset="0.45" stop-color="#4b5263"/>
          <stop offset="1" stop-color="#80838b"/>
        </linearGradient>
        <linearGradient id="footTone" x1="0" y1="0" x2="0" y2="1">
          <stop offset="0" stop-color="#f47a2c"/>
          <stop offset="1" stop-color="#d9401b"/>
        </linearGradient>
      </defs>
      <rect class="hero-photo" x="0" y="0" width="540" height="440" fill="url(#photoTone)" role="img" aria-label="Photo of a smiling worker in a hard hat and overalls holding a coffee cup in a workshop"/>
      <path class="hero-edge" d="M0,282 L384,418 L540,272 L540,290 L384,432 L0,296 Z" fill="var(--orange)"/>
      <path class="content-panel" d="M0,292 L384,426 L540,284 L540,1110 L0,1110 Z" fill="url(#panelTone)"/>
      <path class="footer-band" d="M0,958 C140,940 330,985 540,948 L540,1110 L0,1110 Z" fill="url(#footTone)"/>
      <g class="footer-lines" fill="none" stroke="#ffb07a" stroke-width="1.2" opacity="0.7">
        <path d="M0,968 C150,952 330,994 540,960"/>
        <path d="M0,978 C160,964 340,1000 540,972"/>
        <path d="M0,990 C170,978 350,1006 540,986"/>
      </g>
    </svg>

    <div class="brand-name">CIRCA</div>

    <section class="service service--compliance">
      <svg class="service-icon" viewBox="0 0 50 50" fill="none" stroke="var(--orange)" stroke-width="4">
        <circle cx="25" cy="25" r="13"/>
        <path d="M25 4v8M25 38v8M4 25h8M38 25h8M10 10l6 6M34 34l6 6M40 10l-6 6M16 34l-6 6" stroke-linecap="round"/>
        <path d="M19 31l11-11" stroke-linecap="round"/>
      </svg>
      <h2 class="service-title">COMPLIANCE</h2>
      <p class="service-text">Training and Certifications HR and<br>Safety Onsite Complaince Audit</p>
    </section>

    <section class="service service--claims">
      <svg class="service-icon" viewBox="0 0 50 50" fill="none" stroke="var(--orange)" stroke-width="3">
        <path d="M38 14A16 16 0 0 0 10 18" stroke-linecap="round"/>
        <path d="M12 36A16 16 0 0 0 40 32" stroke-linecap="round"/>
        <path d="M38 6v8h-8M12 44v-8h8" stroke-linecap="round" stroke-linejoin="round"/>
        <text x="25" y="32" text-anchor="middle" font-family="Arimo, Arial, sans-serif" font-size="20" fill="var(--orange)" stroke="none">$</text>
      </svg>
      <h2 class="service-title">CLAIMS</h2>
      <p class="service-text">Immediate, Ongoing Injury and<br>Claims Managemnt</p>
    </section>

    <section class="service service--profit">
      <svg class="service-icon" viewBox="0 0 50 50" fill="none" stroke="var(--orange)" stroke-width="3" stroke-linecap="round">
        <path d="M25 13a10 10 0 0 0-6 18v5h12v-5a10 10 0 0 0-6-18z" fill="var(--orange)" stroke="none"/>
        <path d="M20 40h10M21 44h8"/>
        <path d="M25 3v4M8 10l3 3M42 10l-3 3M3 24h4M43 24h4"/>
      </svg>
      <h2 class="service-title">PROFIT LEAKS</h2>
      <p class="service-text">Detect and Corect Profit Leaks Inherent<br>in Every Work Comp Program That<br>Driver the Cost</p>
    </section>

    <div class="cta-pill">Call Now for more Information</div>
    <div class="cta-phone">555.218.4470</div>
    <div class="site-url">www.circacover.com</div>
  </main>
</body>
</html>
```